Real Estate Investor needs awesome business card design

I invest in real estate, focused on multi-family properties, and I need a business card to hand out to potential partners. I prefer simple, clean designs, but it needs to stand out, so I'd like there to be a bit of red in the design as well.

It should include this information:

Front
Dallin Pecksworth
Real Estate Investor
Direct phone: 502-867-3394
Email: dallinhpecksworth@quillmail.example
Headshot (Picture), I've uploaded a few, just pick the one you think looks best with your design. You can remove the background from the headshot image if it looks better.

Back
The back of the card's design should flow and be congruent with the front. On the back I want to put an inspirational quote or question. There will be different ones depending on the card, so I'll need the original file so I can edit it in the end.

For now, use “The Pessimist Sees Difficulty In Every Opportunity. The Optimist Sees The Opportunity In Every Difficulty.” -Barnaby Ellsworth

Target Market(s)

Investors

Industry/Entity Type

Real Estate

Contact Information for Business Card

Front
Dallin Pecksworth
Real Estate Investor

Back
The back of the card's design should flow and be congruent with the front. On the back I want to put an inspirational quote or question. There will be different ones depending on the card, so I'll need the original file so I can edit it in the end. I've uploaded some EXAMPLES of business cards with quotes on them. Don't copy but feel free to use them as inspiration.

The design will be printed on "ZIB sized" business cards
1039 x 697 pixels
with rounded corners

Font styles to use
Serif
Decorative
Script

Colors
ec1f27

Requirements
Must have
• Headshot, name, and other information in it.
• 1039 x 697 pixels
• Rounded corners
• Clean design that pops. I'm open to see any color background, including black.
• Headshots can be located here: https://www.filecrate.example/sh/8kd2wq7mzt31hvx/BBQTXP4ruf9LmQ0KhcvWx7b?dl=0
Nice to have
• It would be awesome if the design included a personal signature or monogram, but if not I'll get a personal logo developed later and the card redesigned if I think it needs it.
Should not have
• Cluttered design

```html
<!DOCTYPE html>
<html lang="en">
<head>
<meta charset="utf-8">
<title>Dallin Pecksworth — Business Card</title>
<link rel="stylesheet" href="https://fonts.googleapis.com/css2?family=Old+Standard+TT:wght@400;700&display=swap">
<style>
  :root {
    --brand-red: #ec1f27;
    --card-white: #ffffff;
    --ink-grey: #555555;
    --backdrop: #3a3a3a;
    --photo-dark: #1c2a30;
    --photo-mid: #2b3d45;
  }
  * { box-sizing: border-box; margin: 0; padding: 0; }
  html, body {
    width: 1200px; height: 1200px; overflow: hidden;
    background: var(--backdrop);
  }
  .stage {
    width: 1200px; height: 1200px;
    display: flex; flex-direction: column; align-items: center; justify-content: center;
    gap: 60px;
  }
  .card {
    position: relative;
    width: 760px; height: 510px;
    border-radius: 34px;
    overflow: hidden;
    font-family: "Old Standard TT", "Times New Roman", serif;
  }
  /* Front */
  .card--front { background: var(--card-white); }
  .card__band {
    position: absolute; left: 0; right: 0; height: 22px;
    background: var(--brand-red);
  }
  .card__band--top { top: 0; }
  .card__band--bottom { bottom: 0; }
  .headshot {
    position: absolute; left: 470px; top: 76px;
    width: 250px; height: 308px;
    border-radius: 38px;
    background: radial-gradient(ellipse at 45% 35%, var(--photo-mid), var(--photo-dark) 70%);
  }
  .identity { position: absolute; left: 64px; top: 304px; width: 390px; }
  .identity__name {
    color: var(--brand-red);
    font-size: 28px; font-weight: 400;
    letter-spacing: 1px; text-transform: uppercase; line-height: 1;
    white-space: nowrap;
  }
  .identity__title {
    margin-top: 6px;
    color: var(--ink-grey);
    font-size: 15px; letter-spacing: 4px; text-transform: uppercase;
    white-space: nowrap;
  }
  .contact { position: absolute; left: 80px; top: 392px; list-style: none; }
  .contact__item {
    display: flex; align-items: center; gap: 12px;
    color: var(--ink-grey); font-size: 16px; letter-spacing: 0.3px;
    margin-bottom: 12px; white-space: nowrap;
  }
  .contact__icon { width: 20px; height: 20px; flex: none; }
  /* Back */
  .card--back { background: var(--brand-red); }
  .quote {
    position: absolute; left: 78px; top: 150px;
    color: var(--card-white);
    font-size: 29px; letter-spacing: 2px; line-height: 1.45;
    text-transform: uppercase;
  }
  .quote__author { display: block; margin-top: 4px; font-style: normal; }
</style>
</head>
<body>
<main class="stage">
  <section class="card card--front" aria-label="Business card front">
    <div class="card__band card__band--top"></div>
    <div class="card__band card__band--bottom"></div>
    <div class="headshot" role="img" aria-label="Headshot portrait of Dallin Pecksworth on a dark background"></div>
    <div class="identity">
      <h1 class="identity__name">Dallin Pecksworth</h1>
      <p class="identity__title">Real Estate Investor</p>
    </div>
    <ul class="contact">
      <li class="contact__item">
        <svg class="contact__icon" viewBox="0 0 20 20" aria-hidden="true">
          <circle cx="10" cy="10" r="8.5" fill="none" stroke="#ec1f27" stroke-width="1.5"/>
          <rect x="7" y="5" width="6" height="10" rx="1.2" fill="none" stroke="#ec1f27" stroke-width="1.3"/>
          <line x1="9" y1="13" x2="11" y2="13" stroke="#ec1f27" stroke-width="1.2"/>
        </svg>
        502-867-3394
      </li>
      <li class="contact__item">
        <svg class="contact__icon" viewBox="0 0 20 20" aria-hidden="true">
          <circle cx="10" cy="10" r="8.5" fill="none" stroke="#ec1f27" stroke-width="1.5"/>
          <rect x="5.5" y="7" width="9" height="6.5" rx="0.8" fill="#ec1f27"/>
          <polyline points="5.8,7.4 10,10.6 14.2,7.4" fill="none" stroke="#fff" stroke-width="1"/>
        </svg>
        dallinhpecksworth@quillmail.example
      </li>
    </ul>
  </section>

  <section class="card card--back" aria-label="Business card back">
    <blockquote class="quote">
      “The pessimist sees difficulty in<br>
      every opportunity. The optimist<br>
      sees the opportunity in every<br>
      difficulty.”
      <cite class="quote__author">-Barnaby Ellsworth</cite>
    </blockquote>
  </section>
</main>
</body>
</html>
```